Business Card Design Project

I am a property development company requiring a professional looking business card.
The name of the my company is KLV SUMMITRA. I have attached a couple of designs that I have created on my own, that can give you an idea of what I am after.
Above the wording KLV SUMMITRA, I have a orange arc above these words to signify the sun is begining to rise above the horizon.
I have a few designs; Middle Rays, Side Rays, Horizontals Rays which are OK, but I am looking for the better design.
The Rear design of the card is what I had came up with. If you have a better design, I am happy to see it.
The design of the card can follow what I have came up with, or it can be totally different. The fonts needs to be adjusted to another font that is more suitable.
The colours that I have used is what I think I would like to stick with. As I have mentioned, the orange arc is to signify the sun rising. If you have a better colour scheme, I would consider it.
Looking at dealing with first home buyers and proffesional people.
Business

```html
<!DOCTYPE html>
<html lang="en">
<head>
<meta charset="utf-8">
<title>KLV Summitra – Business Cards</title>
<link rel="stylesheet" href="https://fonts.googleapis.com/css2?family=Orbitron:wght@500;600;700&display=swap">
<style>
  :root {
    --bg-light: #b9c8cc;
    --bg-mid: #7f9096;
    --bg-dark: #4b5960;
    --card: #ffffff;
    --ink: #111111;
    --band-cream: #fdf6df;
    --band-lemon: #f5fac4;
    --band-peach: #ff9e63;
    --band-orange: #ff7b3f;
    --band-flame: #ff5a1f;
    --band-red: #ff1d12;
  }
  * { margin: 0; padding: 0; box-sizing: border-box; }
  html, body { width: 1200px; height: 800px; overflow: hidden; }
  body {
    position: relative;
    background: radial-gradient(ellipse 900px 700px at 720px 0px, var(--bg-light) 0%, var(--bg-mid) 50%, var(--bg-dark) 100%);
    font-family: "Orbitron", sans-serif;
    color: var(--ink);
  }
  .card {
    position: absolute;
    width: 606px;
    height: 367px;
    background: var(--card);
    border-radius: 10px;
    overflow: hidden;
    box-shadow: 6px 8px 6px rgba(0, 0, 0, 0.45);
  }
  .card--front { left: 60px; top: 18px; }
  .card--back { left: 505px; top: 410px; }

  .bands {
    position: absolute;
    left: 0; right: 0; bottom: 0;
    height: 103px;
    display: flex;
    flex-direction: column;
  }
  .band { flex: none; }
  .band--cream  { height: 18px; background: var(--band-cream); }
  .band--lemon  { height: 19px; background: var(--band-lemon); }
  .band--peach  { height: 19px; background: var(--band-peach); }
  .band--orange { height: 18px; background: var(--band-orange); }
  .band--flame  { height: 16px; background: var(--band-flame); }
  .band--red    { height: 13px; background: var(--band-red); }

  .brand { position: absolute; line-height: 1; white-space: nowrap; }
  .brand__name { display: block; font-weight: 700; }
  .brand__tagline { display: block; font-weight: 600; }

  .card--front .brand { left: 0; right: 0; top: 126px; text-align: center; }
  .card--front .brand__name { font-size: 47px; letter-spacing: 1px; }
  .card--front .brand__tagline { font-size: 25px; margin-top: 12px; letter-spacing: 0.5px; }

  .card--back .brand { left: 24px; top: 48px; }
  .card--back .brand__name { font-size: 23px; }
  .card--back .brand__tagline { font-size: 12.5px; margin-top: 6px; }

  .holder {
    position: absolute;
    left: 330px; width: 260px;
    top: 22px;
    text-align: center;
    font-weight: 700;
    font-size: 27px;
    line-height: 40px;
    letter-spacing: 1px;
  }

  .contact {
    position: absolute;
    left: 24px; top: 146px;
    list-style: none;
    font-weight: 600;
    font-size: 15.5px;
    line-height: 1;
    z-index: 1;
  }
  .contact li { margin-bottom: 28px; white-space: nowrap; text-shadow: 2px 2px 2px rgba(0,0,0,0.25); }
</style>
</head>
<body>

  <section class="card card--front" aria-label="Business card front">
    <div class="brand">
      <span class="brand__name">KLV Summitra</span>
      <span class="brand__tagline">Property Developments</span>
    </div>
    <div class="bands" aria-hidden="true">
      <div class="band band--cream"></div>
      <div class="band band--lemon"></div>
      <div class="band band--peach"></div>
      <div class="band band--orange"></div>
      <div class="band band--flame"></div>
      <div class="band band--red"></div>
    </div>
  </section>

  <section class="card card--back" aria-label="Business card back">
    <div class="brand">
      <span class="brand__name">KLV Summitra</span>
      <span class="brand__tagline">Property Developments</span>
    </div>
    <div class="holder">
      <p class="holder__name">Marcus Leland</p>
      <p class="holder__role">Director</p>
    </div>
    <ul class="contact">
      <li class="contact__address">48 Wattle Crescent Brookvale NSW 2100 Australia</li>
      <li class="contact__phone">0491 570 156</li>
      <li class="contact__email">marcus@klvsummitra.com.au</li>
      <li class="contact__web">www.klvsummitra.com.au</li>
    </ul>
    <div class="bands" aria-hidden="true">
      <div class="band band--cream"></div>
      <div class="band band--lemon"></div>
      <div class="band band--peach"></div>
      <div class="band band--orange"></div>
      <div class="band band--flame"></div>
      <div class="band band--red"></div>
    </div>
  </section>

</body>
</html>
```